Require an amazing and engaging Home Page redesign! For New Startup!

We require a new design for our home page of www.quonmart.com.au.

We want this to be in a similar theme to the current site, all other pages to remain unchanged however our marketing team have advised that the current home page (initial banner) is not engaging or "hooking" potential leads. I have attached "CRO Recommendations" from our marketing team as an idea to the issues with the Quonmart site.
At the moment we would only like the issues on home page reviewed (Pages: 4 to 10).

I have attached an example from our marketing team as to an idea of how the front home page needs to look.

As an idea of what our competition is doing well please view zestmotors.com.au, drivepeak.com.au (great engagement on home page top banner).

Quonmart is a brand new concept for Australian new car buyers. Quonmart allows a customer buying a new car to receive best price offer for their new car needs and finance requirements all on a sophisticated online dashboard. The dashboard even allows the customer to interact directly with the dealerships to negotiate the price online! (never offered before).

I've provided new logo, brand guidelines for colour and font scheme.

View the website to get an idea of what Quonmart is all about and let's see what we can come up with.

Thanks.

Target Market(s)

Females, age between 21-35

Industry/Entity Type

Automotive

Number of Pages Required

1 page

Requirements
Must have
• Engaging initial banner. We want to see the banner as mocked up and provided but also maybe provide an option showing a large graphic as the banner that incorporates this "hook" for engagement.
• Minimal menu (no Need Help or Newsletter buttons) with new logo on left.
• As per design mockup. Looking for engaging banner.
• Why it Works benefits section - 3 to 4 key benefits
• Customer satisfaction/testimonial area
Nice to have
• As Seen On banner or icon somewhere - maybe near or under the "Get Offers' buttons? As we have been featured in the COASTAL POST

```html
<!DOCTYPE html>
<html lang="en">
<head>
<meta charset="utf-8">
<title>Quonmart – New Car Offers</title>
<link rel="stylesheet" href="https://fonts.googleapis.com/css2?family=Montserrat:wght@400;600;700&family=Open+Sans:wght@400;600;700&family=Oswald:wght@400;500&display=swap">
<style>
:root{
  --navy:#1a4f86;
  --navy-dark:#123d6b;
  --blue:#0d52a5;
  --sky-top:#1f5f90;
  --sky-bottom:#8dbad6;
  --gold:#e3a92a;
  --gold-dark:#c98f16;
  --panel:#e6ebf1;
  --text:#3d4650;
  --muted:#6b7580;
  --footer:#2b7aa9;
  --footer-dark:#1f5d8c;
  --white:#ffffff;
  --line:#d5dbe2;
}
*{box-sizing:border-box;margin:0;padding:0}
html,body{width:1200px;height:3010px;overflow:hidden}
body{font-family:"Open Sans",Arial,sans-serif;color:var(--text);background:var(--white);position:relative}
h1,h2,h3{font-family:"Montserrat",Arial,sans-serif}

/* header */
.site-header{position:absolute;left:0;top:0;width:1200px;height:80px;background:var(--white)}
.brand{position:absolute;left:155px;top:20px;display:flex;align-items:center;gap:10px;font-family:"Montserrat",sans-serif;font-weight:700;font-size:28px;color:var(--navy)}
.brand-dot{width:34px;height:34px;border-radius:50%;background:var(--gold)}
.main-nav{position:absolute;left:390px;top:32px;font-family:"Montserrat",sans-serif;font-size:12px;font-weight:600;color:var(--text)}
.main-nav a{color:inherit;text-decoration:none;position:absolute;white-space:nowrap}
.main-nav .active{color:var(--navy)}
.main-nav .active::after{content:"";position:absolute;left:0;right:0;bottom:-8px;height:2px;background:var(--navy)}
.call-us{position:absolute;left:866px;top:30px;font-family:"Montserrat",sans-serif;font-size:14px;font-weight:600;color:var(--navy);display:flex;align-items:center;gap:8px}
.call-us strong{color:var(--text);font-weight:600}

/* hero */
.hero{position:absolute;left:0;top:80px;width:1200px;height:500px;background:linear-gradient(180deg,var(--sky-top) 0%,#3a7aa8 45%,var(--sky-bottom) 100%);overflow:hidden}
.mascot{position:absolute;left:30px;top:40px;width:240px;height:330px;border-radius:40% 40% 20% 20%;background:linear-gradient(160deg,#c9884a,#e59a2c 60%,#2f6ea4)}
.hero-title{position:absolute;left:382px;top:34px;font-size:29px;font-weight:700;color:var(--white)}
.hero-sub{position:absolute;left:382px;top:72px;font-size:16px;font-weight:600;color:var(--white)}
.steps{position:absolute;left:382px;top:120px;width:662px;height:260px;border:2px solid rgba(255,255,255,.9)}
.step{position:absolute;top:20px;width:200px;text-align:center}
.step-num{width:24px;height:24px;margin:0 auto;border-radius:50%;background:var(--white);color:var(--navy);font-size:11px;font-weight:700;line-height:24px;position:relative;z-index:2}
.step-icon{width:128px;height:128px;margin:-12px auto 0;border-radius:50%;display:flex;align-items:center;justify-content:center}
.step p{margin-top:12px;font-size:13px;line-height:18px;color:var(--white)}
.step-arrow{position:absolute;top:60px}
.btn{display:inline-flex;align-items:center;justify-content:center;gap:8px;height:32px;padding:0 26px;border-radius:16px;font-family:"Montserrat",sans-serif;font-size:11px;font-weight:700;letter-spacing:.5px;color:var(--white);text-decoration:none}
.btn::after{content:"";width:9px;height:9px;border-radius:50%;border:2px solid currentColor}
.btn-navy{background:var(--navy-dark)}
.btn-gold{background:var(--gold)}
.hero .btn{position:absolute;left:646px;top:396px}
.clouds{position:absolute;left:0;bottom:0}

/* section titles */
.section-title{position:absolute;left:0;width:1200px;text-align:center;font-size:18px;font-weight:700;color:var(--navy)}
.section-title.underlined::after{content:"";display:block;width:38px;height:2px;background:var(--navy);margin:10px auto 0}

/* pricing */
.pricing-panel{position:absolute;left:232px;top:716px;width:734px;height:566px;background:var(--panel)}
.plan{position:absolute;top:716px;width:236px;height:566px;text-align:center}
.plan-popular{background:var(--gold);top:700px;height:600px;color:var(--white)}
.popular-tag{position:absolute;left:64px;top:-14px;width:128px;height:28px;background:var(--navy);color:var(--white);font-family:"Montserrat",sans-serif;font-size:10px;font-weight:700;line-height:28px;border:2px solid var(--white)}
.plan-head{margin-top:24px;font-size:14px;line-height:20px;padding:0 20px}
.plan-pin{display:block;margin:14px auto 0}
.plan-features{list-style:none;text-align:left;margin:24px 0 0 22px;font-size:12.5px;line-height:17px;color:var(--muted)}
.plan-popular .plan-features{color:var(--white)}
.plan-features li{position:relative;padding-left:18px;margin-bottom:12px;width:170px}
.plan-features li::before{content:"";position:absolute;left:0;top:3px;width:10px;height:10px;border:1.5px solid currentColor;border-radius:2px}
.plan-features li::after{content:"";position:absolute;left:3px;top:4px;width:4px;height:6px;border:solid currentColor;border-width:0 2px 2px 0;transform:rotate(45deg)}
.plan-select{position:absolute;left:44px;width:150px;height:28px;background:var(--white);border:1px solid var(--line);font-size:11px;color:var(--muted);text-align:left;padding:0 10px;line-height:26px}
.plan-select::after{content:"";position:absolute;right:10px;top:11px;border:4px solid transparent;border-top-color:var(--text)}
.plan-divider{position:absolute;left:20px;right:20px;height:1px;background:var(--line)}
.plan-popular .plan-divider{background:rgba(255,255,255,.5)}
.plan .btn{position:absolute;left:54px;height:32px;padding:0 18px}

/* testimonials */
.slider-arrow{position:absolute;width:16px;height:30px}
.review{position:absolute;top:1404px;width:280px;height:358px;background:var(--white);box-shadow:0 1px 6px rgba(0,0,0,.12);text-align:center;padding:34px 24px 0}
.review.featured{border:2px solid var(--gold);box-shadow:none}
.quote-mark{font-family:"Montserrat",sans-serif;font-size:56px;font-weight:700;line-height:40px;height:40px;color:#b9c1c9}
.review.featured .quote-mark{color:var(--gold)}
.review p{margin-top:18px;font-size:12.5px;line-height:18px;color:var(--muted);height:110px}
.stars{margin-top:26px;font-size:16px;color:var(--navy);letter-spacing:2px}
.review-name{margin-top:10px;font-size:14px;color:var(--text)}
.avatar{width:82px;height:82px;border-radius:50%;margin:12px auto 0;background:linear-gradient(160deg,#c9b39c,#7d6a58)}

/* why it works */
.why{position:absolute;left:0;top:1826px;width:600px;height:350px;background:var(--blue);color:var(--white)}
.why h2{position:absolute;left:0;width:600px;top:46px;text-align:center;font-size:18px;font-weight:700}
.benefit{position:absolute;top:84px;width:130px;text-align:center}
.benefit-num{width:76px;height:76px;margin:0 auto;border:2px solid var(--white);border-radius:50%;font-family:"Montserrat",sans-serif;font-size:20px;font-weight:600;line-height:72px}
.benefit p{margin-top:14px;font-size:12.5px;line-height:17px}
.why .btn{position:absolute;left:306px;top:272px;height:34px}
.why-video{position:absolute;left:600px;top:1826px;width:600px;height:350px;background:linear-gradient(100deg,#5b7fa2 0%,#9fb4c5 45%,#2f3a47 100%)}

/* live deals */
.deals-sub{position:absolute;left:0;width:1200px;top:2252px;text-align:center;font-size:15px;color:var(--text)}
.deal{position:absolute;top:2306px;width:204px;height:158px;background:var(--panel)}
.deal-price{position:absolute;left:0;top:0;width:48px;height:48px;background:var(--gold);color:var(--white);font-family:"Montserrat",sans-serif;font-weight:700;font-size:12px;line-height:14px;text-align:center;padding-top:8px}
.deal-price small{display:block;font-size:9px;font-weight:600}
.deal-name{position:absolute;left:74px;top:12px;font-family:"Montserrat",sans-serif;font-weight:700;font-size:13.5px;color:var(--navy)}
.deal-car{position:absolute;left:22px;top:50px;width:160px;height:70px;border-radius:40px 60px 14px 14px;background:linear-gradient(180deg,#6c7077,#2e3136)}
.deal-save{position:absolute;left:0;width:204px;top:132px;text-align:center;font-size:11px;font-weight:700;color:var(--text)}

/* footer */
.site-footer{position:absolute;left:0;top:2514px;width:1200px;height:406px;background:var(--footer);color:var(--white)}
.footer-title{position:absolute;font-family:"Montserrat",sans-serif;font-size:13px;font-weight:700}
.contact{position:absolute;left:156px;top:92px;width:280px;font-size:12.5px;line-height:18px}
.contact dt{font-weight:700;margin-top:16px}
.contact dt:first-child{margin-top:0}
.contact dd{margin-top:6px}
.contact a{color:var(--white)}
.social{display:flex;gap:10px;margin-top:8px}
.social span{width:10px;height:10px;border-radius:50%;background:var(--white)}
.field{position:absolute;height:34px;border:1px solid rgba(255,255,255,.55);font-size:11px;color:rgba(255,255,255,.85);padding:0 10px;line-height:32px}
.field.select::after{content:"";position:absolute;right:10px;top:14px;border:4px solid transparent;border-top-color:var(--white)}
.submit-btn{position:absolute;left:510px;top:318px;height:34px}
.footer-bar{position:absolute;left:0;top:2920px;width:1200px;height:90px;background:var(--footer-dark);color:var(--white);font-size:12px}
.footer-bar .copy{position:absolute;left:152px;top:18px}
.footer-links{position:absolute;left:152px;top:44px;display:flex;gap:6px}
.footer-links a{color:var(--white);text-decoration:none}
.footer-links a.current{color:var(--gold);text-decoration:underline}
.to-top{position:absolute;left:1004px;top:24px;width:34px;height:30px;border:1.5px solid var(--gold)}
</style>
</head>
<body>

<header class="site-header">
  <div class="brand"><span class="brand-dot"></span>Quonmart</div>
  <nav class="main-nav">
    <a style="left:0">HOW IT WORKS</a>
    <a class="active" style="left:126px">PRICING</a>
    <a style="left:210px">FAQ</a>
    <a style="left:266px">APPLY</a>
    <a style="left:344px">LOGIN</a>
  </nav>
  <div class="call-us">CALL US
    <svg width="10" height="16" viewBox="0 0 10 16"><rect x="1" y="1" width="8" height="14" rx="1.5" fill="none" stroke="#1a4f86" stroke-width="1.6"/><circle cx="5" cy="12.5" r="1" fill="#1a4f86"/></svg>
    <strong>1300-482-910</strong></div>
</header>

<section class="hero">
  <div class="mascot" role="img" aria-label="Cartoon superhero dog mascot in a blue suit and orange cape holding car keys"></div>
  <h1 class="hero-title">A Revolution In Car Buying Has Arrived</h1>
  <p class="hero-sub">Get car dealers and lenders to bid for Your business today.</p>
  <div class="steps">
    <div class="step" style="left:-12px">
      <div class="step-num">1</div>
      <div class="step-icon" style="background:#3f86b7">
        <svg width="64" height="44" viewBox="0 0 64 44"><rect x="8" y="2" width="48" height="32" rx="2" fill="#2b3d52"/><rect x="11" y="5" width="42" height="26" fill="#dfe8f0"/><rect x="2" y="34" width="60" height="5" rx="2" fill="#c9d3dc"/></svg>
      </div>
      <p>Submit your car or<br>finance needs</p>
    </div>
    <svg class="step-arrow" style="left:176px" width="60" height="30" viewBox="0 0 60 30"><path d="M4 26 Q30 0 54 14" fill="none" stroke="#fff" stroke-width="2"/><path d="M48 8 L56 15 L46 18" fill="none" stroke="#fff" stroke-width="2"/></svg>
    <div class="step" style="left:216px">
      <div class="step-num">2</div>
      <div class="step-icon" style="background:var(--gold)">
        <svg width="50" height="50" viewBox="0 0 50 50"><rect x="8" y="6" width="18" height="26" rx="6" fill="#2b3d52" transform="rotate(-30 17 19)"/><rect x="24" y="26" width="6" height="22" rx="2" fill="#c9d3dc" transform="rotate(-30 27 37)"/></svg>
      </div>
      <p>Dealerships &amp; lenders<br>submit their best offers</p>
    </div>
    <svg class="step-arrow" style="left:404px" width="60" height="30" viewBox="0 0 60 30"><path d="M4 26 Q30 0 54 14" fill="none" stroke="#fff" stroke-width="2"/><path d="M48 8 L56 15 L46 18" fill="none" stroke="#fff" stroke-width="2"/></svg>
    <div class="step" style="left:444px">
      <div class="step-num">3</div>
      <div class="step-icon" style="background:#2f3a47">
        <svg width="76" height="34" viewBox="0 0 76 34"><path d="M4 22 L10 12 L26 10 L36 2 L56 4 L66 14 L72 16 L72 24 L4 24 Z" fill="#f1c232"/><circle cx="18" cy="25" r="6" fill="#1c232b"/><circle cx="58" cy="25" r="6" fill="#1c232b"/></svg>
      </div>
      <p>Choose the best deals &amp; ex-<br>change contact details. It's<br>that easy!</p>
    </div>
  </div>
  <a class="btn btn-navy">GET OFFERS</a>
  <svg class="clouds" width="1200" height="110" viewBox="0 0 1200 110"><path d="M0 110 V70 Q30 40 70 60 Q100 20 150 50 Q190 30 220 60 Q260 40 300 70 Q340 60 380 80 L820 80 Q860 50 900 60 Q930 20 980 40 Q1020 10 1060 40 Q1100 20 1140 50 Q1180 40 1200 60 V110 Z" fill="#fff"/></svg>
</section>

<h2 class="section-title underlined" style="top:620px">OUR PRICING</h2>
<div class="pricing-panel"></div>

<div class="plan" style="left:234px">
  <p class="plan-head">I just need the best deals on a new car.</p>
  <svg class="plan-pin" width="98" height="112" viewBox="0 0 98 112"><path d="M49 110 C49 110 2 72 2 47 A47 47 0 0 1 96 47 C96 72 49 110 49 110Z" fill="#2f79aa"/><text x="49" y="60" text-anchor="middle" font-family="Oswald,sans-serif" font-size="36" fill="#fff"><tspan font-size="16" dy="-14">$</tspan><tspan dy="14">47</tspan></text></svg>
  <ul class="plan-features"><li>3 dealership BEST PRICE car quotes</li></ul>
  <div class="plan-select" style="top:404px">Car Model</div>
  <div class="plan-select" style="top:444px">Car Make</div>
  <div class="plan-divider" style="top:482px"></div>
  <a class="btn btn-navy" style="top:508px">GET OFFERS</a>
</div>

<div class="plan plan-popular" style="left:470px">
  <div class="popular-tag">MOST POPULAR</div>
  <p class="plan-head" style="margin-top:40px">I just need the best deals on a new car &nbsp;and finance.</p>
  <svg class="plan-pin" width="98" height="112" viewBox="0 0 98 112"><path d="M49 110 C49 110 2 72 2 47 A47 47 0 0 1 96 47 C96 72 49 110 49 110Z" fill="#fff"/><text x="49" y="60" text-anchor="middle" font-family="Oswald,sans-serif" font-size="36" fill="#1a4f86"><tspan font-size="16" dy="-14">$</tspan><tspan dy="14">47</tspan></text></svg>
  <ul class="plan-features"><li>3 dealership BEST PRICE car quotes</li><li>3 live loan quotes from our broker panel</li></ul>
  <div class="plan-select" style="top:420px;left:46px">Car Model</div>
  <div class="plan-select" style="top:460px;left:46px">Car Make</div>
  <div class="plan-divider" style="top:500px"></div>
  <a class="btn btn-navy" style="top:524px;left:58px">GET OFFERS</a>
</div>

<div class="plan" style="left:730px">
  <p class="plan-head">I just need the best deals on a new car</p>
  <svg class="plan-pin" width="98" height="112" viewBox="0 0 98 112"><path d="M49 110 C49 110 2 72 2 47 A47 47 0 0 1 96 47 C96 72 49 110 49 110Z" fill="#2f79aa"/><text x="49" y="60" text-anchor="middle" font-family="Oswald,sans-serif" font-size="36" fill="#fff"><tspan font-size="16" dy="-14">$</tspan><tspan dy="14">7</tspan></text></svg>
  <ul class="plan-features"><li>Perfect for NEW OR USED cars</li><li>Receive up to 3 live loan quotes</li><li>Guaranteed to beat dealership finance</li><li>Quotes from our award winning broker panel</li></ul>
  <div class="plan-select" style="top:404px">Car Model</div>
  <div class="plan-select" style="top:444px">Car Make</div>
  <div class="plan-divider" style="top:482px"></div>
  <a class="btn btn-navy" style="top:508px">GET OFFERS</a>
</div>

<h2 class="section-title" style="top:1340px">SEE WHAT OUR CUSTOMERS SAYS</h2>
<svg class="slider-arrow" style="left:114px;top:1568px" viewBox="0 0 16 30"><path d="M14 2 L2 15 L14 28" fill="none" stroke="#555" stroke-width="2"/></svg>
<svg class="slider-arrow" style="left:1066px;top:1568px" viewBox="0 0 16 30"><path d="M2 2 L14 15 L2 28" fill="none" stroke="#e3a92a" stroke-width="2"/></svg>

<article class="review" style="left:156px">
  <div class="quote-mark">&ldquo;</div>
  <p>Quonmart was able to save me over $7,000 off the price of my new Torvan Grand Ridge for me &amp; my husband through their bid contest - they also showed me an amazing finance offer I didn't even know was available</p>
  <div class="stars">★★★☆☆</div>
  <div class="review-name">Leanne, Oakfield Ridge</div>
  <div class="avatar" role="img" aria-label="Customer portrait photo"></div>
</article>
<article class="review featured" style="left:458px">
  <div class="quote-mark">&ldquo;</div>
  <p>Totally blown away with my experience with Quonmart. They were able to get me a super sharp price on the new Kestrel work ute and I got a great bundle deal on the loan with a professional broker.</p>
  <div class="stars">★★★☆☆</div>
  <div class="review-name">Dylan, Seacliff Bay</div>
  <div class="avatar" role="img" aria-label="Customer portrait photo"></div>
</article>
<article class="review" style="left:760px">
  <div class="quote-mark">&ldquo;</div>
  <p>Quonmart was able to save me over $7,000 off the price of my new Torvan Grand Ridge for me &amp; my husband through their bid contest - they also showed me an amazing finance offer I didn't even know was available</p>
  <div class="stars">★★★☆☆</div>
  <div class="review-name">Leanne, Oakfield Ridge</div>
  <div class="avatar" role="img" aria-label="Customer portrait photo"></div>
</article>

<section class="why">
  <h2>WHY IT WORKS</h2>
  <div class="benefit" style="left:156px"><div class="benefit-num">01</div><p>Have local dealer-ships competing for your...</p></div>
  <div class="benefit" style="left:308px"><div class="benefit-num">02</div><p>Award-winning brokers show you their best...</p></div>
  <div class="benefit" style="left:460px"><div class="benefit-num">03</div><p>A refined and easy sign-up process with an...</p></div>
  <a class="btn btn-gold">GET OFFERS</a>
</section>
<div class="why-video" role="img" aria-label="Video still of a person watching the Quonmart promo on a desktop screen, with a play button"></div>

<h2 class="section-title" style="top:2218px">LIVE DEALS</h2>
<p class="deals-sub">Our average clintes saved nearly 14% off the list price</p>
<svg class="slider-arrow" style="left:114px;top:2346px" viewBox="0 0 16 30"><path d="M14 2 L2 15 L14 28" fill="none" stroke="#555" stroke-width="2"/></svg>
<svg class="slider-arrow" style="left:1066px;top:2346px" viewBox="0 0 16 30"><path d="M2 2 L14 15 L2 28" fill="none" stroke="#e3a92a" stroke-width="2"/></svg>

<div class="deal" style="left:156px"><div class="deal-price">$89<small>week</small></div><div class="deal-name">Veltra ST</div><div class="deal-car" role="img" aria-label="Dark grey sedan photo"></div><div class="deal-save">($6,150 OFF Retail price)</div></div>
<div class="deal" style="left:382px"><div class="deal-price">$89<small>week</small></div><div class="deal-name">Veltra ST</div><div class="deal-car" role="img" aria-label="Dark grey sedan photo"></div><div class="deal-save">($6,150 OFF Retail price)</div></div>
<div class="deal" style="left:610px"><div class="deal-price">$89<small>week</small></div><div class="deal-name">Veltra ST</div><div class="deal-car" role="img" aria-label="Dark grey sedan photo"></div><div class="deal-save">($6,150 OFF Retail price)</div></div>
<div class="deal" style="left:836px"><div class="deal-price">$89<small>week</small></div><div class="deal-name">Veltra ST</div><div class="deal-car" role="img" aria-label="Dark grey sedan photo"></div><div class="deal-save">($6,150 OFF Retail price)</div></div>

<footer class="site-footer">
  <h3 class="footer-title" style="left:156px;top:52px">CONTACT US</h3>
  <dl class="contact">
    <dt>ADDRESS :</dt><dd>The standard chunk Lorem Ipsum used<br>the 1500s. 12340</dd>
    <dt>PHONE :</dt><dd>1300-482-910</dd>
    <dt>EMAIL :</dt><dd><a>info@quonmart.com.au</a></dd>
    <dt>FOLLOW US :</dt><dd class="social"><span></span><span></span><span></span><span></span></dd>
  </dl>
  <h3 class="footer-title" style="left:510px;top:52px">GET IN TOUCH</h3>
  <div class="field" style="left:510px;top:104px;width:256px">First name</div>
  <div class="field" style="left:784px;top:104px;width:256px">Last name</div>
  <div class="field" style="left:510px;top:150px;width:256px">Phone</div>
  <div class="field" style="left:784px;top:150px;width:256px">Email</div>
  <div class="field select" style="left:510px;top:196px;width:256px">Preferred contact method</div>
  <div class="field select" style="left:784px;top:196px;width:256px">I have a question regarding</div>
  <div class="field" style="left:510px;top:244px;width:530px;height:64px">Message</div>
  <a class="btn btn-gold submit-btn">SUBMIT</a>
</footer>

<div class="footer-bar">
  <p class="copy">©2017 Quonmart.com.au. All Rights Reserved.</p>
  <nav class="footer-links">
    <a class="current">How it works</a> / <a>Pricing</a> / <a>FAQ</a> / <a>Privacy Policy</a> / <a>Terms and Conditions</a> / <a>Car Reviews</a> / <a>Become a Supplier</a>
  </nav>
  <div class="to-top"><svg width="31" height="27" viewBox="0 0 31 27"><path d="M15.5 20 V7 M9 13 L15.5 6 L22 13" fill="none" stroke="#e3a92a" stroke-width="1.8"/></svg></div>
</div>

</body>
</html>
```